Multi brand diverse distributor requires new business card

We're a distributor representing multiple brands and would like a new business card reflecting our diversity.

We incorporate landscape architecture, environmental engineering and sustainability into construction projects.

KV Group is the company name, and therefore the KV logo should be the primary logo.

Target Market(s)

Engineers, Landscape Architects, Environmental

Contact Information for Business Card

See sample

Colors

Designer to choose colors to be used in the design.

```html
<!DOCTYPE html>
<html lang="en">
<head>
<meta charset="utf-8">
<title>KV Group — Business Card</title>
<link rel="stylesheet" href="https://fonts.googleapis.com/css2?family=Montserrat:wght@400;500;600;700;800&display=swap">
<style>
  :root {
    --backdrop: #3a3a3a;
    --card-white: #ffffff;
    --card-black: #161616;
    --brand-red: #c0223f;
    --ink-grey: #555555;
    --soft-grey: #7a7a7a;
    --partner-blue: #2f7fc8;
    --partner-light: #e9e9e9;
  }
  * { box-sizing: border-box; margin: 0; padding: 0; }
  html, body {
    width: 1200px; height: 801px; overflow: hidden;
    background: var(--backdrop);
    font-family: "Montserrat", sans-serif;
  }
  .stage {
    width: 1200px; height: 801px;
    display: flex; align-items: center; justify-content: center; gap: 40px;
  }
  .card {
    position: relative;
    width: 525px; height: 300px;
    border-bottom: 3px solid var(--brand-red);
    box-shadow: 0 10px 24px rgba(0,0,0,.35);
    overflow: hidden;
  }
  /* Front */
  .card-front { background: var(--card-white); }
  .brand-block {
    position: absolute; left: 58px; top: 78px; width: 180px;
  }
  .brand-mark {
    display: flex; align-items: center; gap: 10px;
    color: var(--brand-red); font-weight: 800; font-size: 36px; letter-spacing: -.5px;
  }
  .brand-mark .mark-square {
    width: 18px; height: 18px; background: var(--brand-red); flex: none;
  }
  .brand-rule {
    margin-top: 12px; height: 1.5px; background: var(--brand-red); width: 170px;
  }
  .brand-est {
    margin-top: 8px; text-align: right; padding-right: 10px;
    font-size: 11px; font-weight: 600; letter-spacing: 2px; color: #222;
  }
  .divider {
    position: absolute; left: 262px; top: 62px; width: 1px; height: 110px;
    background: var(--brand-red);
  }
  .contact-block { position: absolute; left: 286px; top: 64px; }
  .person-name {
    color: var(--brand-red); font-weight: 700; font-size: 16px; letter-spacing: .3px;
  }
  .person-title { margin-top: 3px; font-size: 11px; color: var(--ink-grey); }
  .contact-list { list-style: none; margin-top: 10px; }
  .contact-list li {
    display: flex; align-items: center; gap: 8px;
    font-size: 11.5px; color: var(--ink-grey); line-height: 19px;
  }
  .contact-list svg { width: 11px; height: 11px; fill: var(--brand-red); flex: none; }
  .office-list {
    position: absolute; left: 0; right: 0; bottom: 34px;
    text-align: center; font-size: 12.5px; color: var(--soft-grey); letter-spacing: .3px;
  }
  .office-list .dot { color: var(--brand-red); margin: 0 6px; }

  /* Back */
  .card-back { background: var(--card-black); }
  .pattern-field {
    position: absolute; inset: 0;
    background: linear-gradient(160deg, #1c1c1c 0%, #262626 50%, #1a1a1a 100%);
  }
  .partner-row {
    position: absolute; right: 34px; bottom: 44px;
    display: flex; align-items: center; gap: 34px;
  }
  .partner-name {
    font-weight: 700; font-size: 18px; color: var(--partner-light);
    display: flex; align-items: center; gap: 8px;
  }
  .partner-name .partner-dot {
    width: 12px; height: 12px; border-radius: 50%; background: var(--partner-blue);
  }
</style>
</head>
<body>
<main class="stage">

  <section class="card card-front" aria-label="Business card front">
    <div class="brand-block">
      <div class="brand-mark"><span class="mark-square"></span>KV Group</div>
      <div class="brand-rule"></div>
      <div class="brand-est">EST. 1971</div>
    </div>

    <div class="divider"></div>

    <div class="contact-block">
      <h1 class="person-name">MARCO BELLANI</h1>
      <p class="person-title">B.Eng (Civil)</p>
      <ul class="contact-list">
        <li>
          <svg viewBox="0 0 24 24" aria-hidden="true"><path d="M6.6 10.8a15.1 15.1 0 0 0 6.6 6.6l2.2-2.2a1 1 0 0 1 1-.25 11.4 11.4 0 0 0 3.6.57 1 1 0 0 1 1 1V20a1 1 0 0 1-1 1A17 17 0 0 1 3 4a1 1 0 0 1 1-1h3.5a1 1 0 0 1 1 1c0 1.25.2 2.45.57 3.6a1 1 0 0 1-.25 1z"/></svg>
          0400 123 456
        </li>
        <li>
          <svg viewBox="0 0 24 24" aria-hidden="true"><path d="M7 1h10a2 2 0 0 1 2 2v18a2 2 0 0 1-2 2H7a2 2 0 0 1-2-2V3a2 2 0 0 1 2-2zm0 3v14h10V4z"/></svg>
          1300 000 123
        </li>
        <li>
          <svg viewBox="0 0 24 24" aria-hidden="true"><path d="M2 5h20v14H2zm2 2v.5l8 5 8-5V7z"/></svg>
          marco@kvgroup.com.au
        </li>
        <li>
          <svg viewBox="0 0 24 24" aria-hidden="true"><path d="M12 2a10 10 0 1 0 0 20 10 10 0 0 0 0-20zm6.9 9h-3a15 15 0 0 0-1.4-6 8 8 0 0 1 4.4 6zM12 4.1c.9 1.3 1.7 3.6 1.9 6.9h-3.8c.2-3.3 1-5.6 1.9-6.9zM9.5 5a15 15 0 0 0-1.4 6h-3a8 8 0 0 1 4.4-6zm-4.4 8h3a15 15 0 0 0 1.4 6 8 8 0 0 1-4.4-6zm6.9 6.9c-.9-1.3-1.7-3.6-1.9-6.9h3.8c-.2 3.3-1 5.6-1.9 6.9zm2.5-.9a15 15 0 0 0 1.4-6h3a8 8 0 0 1-4.4 6z"/></svg>
          www.kvgroup.com.au
        </li>
      </ul>
    </div>

    <p class="office-list">
      Adelaide<span class="dot">•</span>Brisbane<span class="dot">•</span>Melbourne<span class="dot">•</span>Perth<span class="dot">•</span>Sydney
    </p>
  </section>

  <section class="card card-back" aria-label="Business card back">
    <div class="pattern-field" role="img" aria-label="Tonal repeating KV monogram pattern covering the card"></div>
    <div class="partner-row">
      <span class="partner-name">Terrafibre</span>
      <span class="partner-name"><span class="partner-dot"></span>Aquaflow</span>
    </div>
  </section>

</main>
</body>
</html>
```